Engineering Consultant Business Card

I'm starting a new business as a high-end engineering consultant in a niche field. I've attached the jpg for my logo plus the branding guideline document that I've been following. You can see my business website here: www.tarvikworks.com
I'd like a business card that has the logo on one side, then the other side has (in any order): Tarvik Works, Inc.
Dana Whitlock
President and Chief EMC Engineer
www.tarvikworks.com
dana@tarvikworks.com
Optional: motto "We will solve your EMC problems as early as possible—ideally before they even start."
I'm not planning on including a phone number
Target Market(s)
Businesses, especially makers of electronics hardware
Industry/Entity Type
Electrical engineering
Contact Information for Business Card
Company name, my name, website, email

```html
<!DOCTYPE html>
<html lang="en">
<head>
<meta charset="utf-8">
<title>Tarvik Works, Inc. — Business Card</title>
<link href="https://fonts.googleapis.com/css2?family=Montserrat:wght@700&family=Catamaran:wght@400;700&display=swap" rel="stylesheet">
<style>
  :root {
    --brand-blue: #2f4a98;
    --ink: #2a2a2a;
    --paper: #ffffff;
    --backdrop: #3a3a3a;
  }
  * { margin: 0; padding: 0; box-sizing: border-box; }
  html, body {
    width: 1200px;
    height: 1059px;
    overflow: hidden;
    background: var(--backdrop);
  }
  .canvas {
    position: relative;
    width: 1200px;
    height: 1059px;
  }
  .card {
    position: absolute;
    width: 690px;
    height: 392px;
    border-radius: 24px;
    overflow: hidden;
  }
  .card-front {
    left: 256px;
    top: 100px;
    background: var(--paper);
  }
  .card-back {
    left: 254px;
    top: 537px;
    background: var(--brand-blue);
    display: flex;
    align-items: center;
    justify-content: center;
    gap: 18px;
  }
  .wordmark {
    position: absolute;
    left: 33px;
    top: 62px;
    font-family: "Montserrat", sans-serif;
    font-weight: 700;
    font-size: 78px;
    letter-spacing: -1px;
    line-height: 1;
    color: var(--brand-blue);
  }
  .contact-block {
    position: absolute;
    left: 33px;
    top: 225px;
    font-family: "Catamaran", sans-serif;
    color: var(--ink);
  }
  .person-name {
    font-weight: 700;
    font-size: 30px;
    line-height: 1.1;
    color: var(--brand-blue);
    letter-spacing: 0.2px;
  }
  .person-title {
    font-weight: 400;
    font-size: 16.5px;
    line-height: 1.3;
    letter-spacing: 0.3px;
    margin-top: 2px;
  }
  .divider {
    width: 10px;
    height: 1.5px;
    background: var(--brand-blue);
    margin: 13px 0 17px;
  }
  .contact-line {
    display: flex;
    align-items: center;
    gap: 9px;
    font-size: 17px;
    letter-spacing: 0.4px;
    line-height: 1;
    margin-bottom: 12px;
  }
  .contact-line svg { width: 13px; height: 13px; flex: none; }
  .back-mark-ring {
    width: 46px;
    height: 46px;
    border: 6px solid var(--paper);
    border-radius: 50%;
  }
  .back-mark-name {
    font-family: "Montserrat", sans-serif;
    font-weight: 700;
    font-size: 48px;
    letter-spacing: -0.5px;
    line-height: 1;
    color: var(--paper);
  }
</style>
</head>
<body>
<main class="canvas">
  <section class="card card-front" aria-label="Card front">
    <div class="wordmark">TWI</div>
    <div class="contact-block">
      <h1 class="person-name">Dana Whitlock</h1>
      <p class="person-title">President &amp; Chief EMC Engineer</p>
      <div class="divider"></div>
      <p class="contact-line">
        <svg viewBox="0 0 16 16" aria-hidden="true"><rect x="1" y="3" width="14" height="10" rx="1.5" fill="var(--brand-blue)"/><path d="M2 4.5 L8 9 L14 4.5" fill="none" stroke="#fff" stroke-width="1.4"/></svg>
        dana@tarvikworks.com
      </p>
      <p class="contact-line">
        <svg viewBox="0 0 16 16" aria-hidden="true" fill="none" stroke="var(--brand-blue)" stroke-width="1.3"><circle cx="8" cy="8" r="6.5"/><ellipse cx="8" cy="8" rx="2.8" ry="6.5"/><path d="M1.5 8h13M2.5 4.8h11M2.5 11.2h11"/></svg>
        www.tarvikworks.com
      </p>
    </div>
  </section>

  <section class="card card-back" aria-label="Card back">
    <div class="back-mark-ring" aria-hidden="true"></div>
    <div class="back-mark-name">TWI</div>
  </section>
</main>
</body>
</html>
```